Biz Cards

Please design new business cards. The colors are black and white

I'm in a meeting all day and will look at all these options tomorrow.

Industry/Entity Type

Flexible Office Space

Contact Information for Business Card

add the tag line- "Upgrade your workday."

Colors

Designer to choose only greyscale colors for use in the design.

Requirements
Must have
• Logo, contact name, phone number, email, website on one side. Upgrade your workday. QR code to website on the other side.

```html
<!DOCTYPE html>
<html lang="en">
<head>
<meta charset="utf-8">
<title>Nova Private Offices – Business Card</title>
<link href="https://fonts.googleapis.com/css2?family=Montserrat:wght@400;600;700&display=swap" rel="stylesheet">
<style>
  :root {
    --backdrop: #2c2c2c;
    --card-top: #1c1c1c;
    --card-bottom: #2a2a2a;
    --ink: #e6e6e6;
    --ink-soft: #cfcfcf;
    --brand: #7a7a7a;
    --shadow: rgba(0, 0, 0, 0.45);
  }
  * { margin: 0; padding: 0; box-sizing: border-box; }
  html, body {
    width: 1200px;
    height: 1138px;
    overflow: hidden;
    background: var(--backdrop);
    font-family: "Montserrat", sans-serif;
  }
  .canvas {
    position: relative;
    width: 1200px;
    height: 1138px;
  }
  .card {
    position: absolute;
    border-radius: 16px;
    background: linear-gradient(160deg, var(--card-top) 0%, var(--card-bottom) 100%);
    box-shadow: 0 8px 14px var(--shadow);
    color: var(--ink);
    text-align: center;
  }
  .card--front { left: 274px; top: 186px; width: 624px; height: 376px; }
  .card--back  { left: 276px; top: 608px; width: 620px; height: 374px; }

  .brand-name {
    position: absolute;
    left: 0; right: 0;
    top: 152px;
    font-size: 34px;
    font-weight: 600;
    letter-spacing: 0.14em;
    color: var(--brand);
  }
  .tagline {
    position: absolute;
    left: 0; right: 0;
    top: 328px;
    font-size: 15px;
    font-weight: 700;
    letter-spacing: 0.04em;
    color: var(--ink);
  }

  .contact-name {
    position: absolute;
    left: 0; right: 0;
    top: 228px;
    font-size: 24px;
    font-weight: 700;
    letter-spacing: 0.01em;
  }
  .contact-role {
    position: absolute;
    left: 0; right: 0;
    top: 259px;
    font-size: 15px;
    font-weight: 400;
    color: var(--ink-soft);
    letter-spacing: 0.02em;
  }
  .contact-lines {
    position: absolute;
    left: 0; right: 0;
    top: 287px;
    display: flex;
    justify-content: center;
    gap: 22px;
    font-size: 15.5px;
    color: var(--ink-soft);
  }
  .contact-item { display: flex; align-items: center; gap: 9px; }
  .contact-item svg { width: 15px; height: 15px; fill: none; stroke: var(--ink-soft); stroke-width: 1.6; }
  .contact-item svg.solid { fill: var(--ink-soft); stroke: none; }
  .contact-address {
    position: absolute;
    left: 0; right: 0;
    top: 313px;
    font-size: 15.5px;
    color: var(--ink-soft);
  }
</style>
</head>
<body>
<main class="canvas">
  <section class="card card--front">
    <div class="brand-name">NOVA PRIVATE OFFICES</div>
    <div class="tagline">UPGRADE YOUR WORKDAY</div>
  </section>

  <section class="card card--back">
    <div class="contact-name">JORDAN VALE</div>
    <div class="contact-role">Managing Director</div>
    <div class="contact-lines">
      <span class="contact-item">
        <svg class="solid" viewBox="0 0 16 16" aria-hidden="true"><path d="M3 4c0-1 1-2 5-2s5 1 5 2v1.5h-3V4.3H6v1.2H3zM4 7h8l1 6H3z"/></svg>
        000-0000-000
      </span>
      <span class="contact-item">
        <svg viewBox="0 0 16 16" aria-hidden="true"><rect x="1.5" y="3.5" width="13" height="9" class="solid" style="fill:var(--ink-soft);stroke:none"/><path d="M1.5 3.5 8 9l6.5-5.5" stroke="#222"/></svg>
        sale@novaoffices.com
      </span>
      <span class="contact-item">
        <svg viewBox="0 0 16 16" aria-hidden="true"><circle cx="8" cy="8" r="6.3"/><ellipse cx="8" cy="8" rx="2.8" ry="6.3"/><path d="M1.7 8h12.6M2.6 5h10.8M2.6 11h10.8"/></svg>
        novaoffices.com
      </span>
    </div>
    <div class="contact-address">123 Anywhere, Any City, Any Town, US 012345</div>
  </section>
</main>
</body>
</html>
```